Product label for herbal salves, lotions, soaps and tinctures

We need a very simple, clean and organic looking label that can be used for an ointment jar, a lotion bottle and a dropper bottle.
We have an existing logo (see attached). We like the colors white, olive green, gold and black. It needs to include product name as dominant and logo. It also needs to include an ingredient list, and usage statement. Include weight of product, distributed by, made in the USA, and NQB statement.
Example of what needs to be present:
Logo
Name: Calmwick Balm
Used for: For Muscle Aches, Arthritis, Tendonitis, Headaches
To Use: For muscle aches, arthritis and tendonitis, massage into affected area. For tension headache apply to neck, temples and forehead.
Store in a cool and dry place, away from direct heat and sunlight.
Weight of product: 1.75
DIST. BY: Brookmere Herbal
Made in the USA
This product is not intended to diagnose, treat, cure
or prevent any disease. Not regulated
by the NQB. Please consult your health care practitioner
before using product. Discontinue use if any adverse reaction occurs.
Ingredient list:
Wildcrafted Ingredients:
Ashwagandha Root, Peppermint Leaf, Hops Flowers, St. John’s Wort Herb, Arnica Flowers, Green Tea Leaf, Alfalfa Leaf, Dandelion Root, Burdock Root, Chickweed Herb, Chaparral Leaf, Yarrow Flowers, Boneset Herb, Moringa Leaf, Meadowsweet Herb, Nettle Leaf
Organic Ingredients:
Olive Oil, Aloe Leaf, Sweet Birch Bark, Helichrysum Flowers, Holy Basil Leaf, Borage Herb, Ginger Root, Angelica Root, White Willow Bark, Mustard Seed, Beeswax, Vitamin E, Essential Oils
Dimensions of Jar:
Circumference: 7 in.
Height: 1 in.

```html
<!DOCTYPE html>
<html lang="en">
<head>
<meta charset="utf-8">
<title>Calmwick Balm – Jar Label</title>
<link href="https://fonts.googleapis.com/css2?family=Barlow:wght@500;600&family=Manrope:wght@400;600;700&display=swap" rel="stylesheet">
<style>
  :root {
    --paper: #ffffff;
    --ink: #141414;
    --olive: #6b7a2e;
    --olive-soft: #7d8a45;
    --rule: #222222;
  }
  * { box-sizing: border-box; margin: 0; padding: 0; }
  html, body { width: 1200px; height: 1157px; overflow: hidden; background: var(--paper); }
  body { position: relative; font-family: "Manrope", sans-serif; color: var(--ink); }

  .label {
    position: absolute;
    left: 20px;
    top: 500px;
    width: 1160px;
    height: 140px;
    font-size: 10.6px;
    line-height: 12px;
  }

  .ingredients {
    position: absolute; left: 0; top: 0; width: 333px;
    text-align: justify;
  }
  .ingredients h3 { font-size: 10.6px; font-weight: 700; }
  .ingredients h4 { font-size: 10.6px; font-weight: 600; font-style: italic; color: var(--olive); }

  .brand-panel { position: absolute; left: 390px; top: 0; width: 340px; height: 140px; }
  .product-name {
    position: absolute; left: 0; top: 16px; width: 330px; text-align: center;
    font-family: "Barlow", sans-serif; font-weight: 600; font-size: 25px;
    letter-spacing: 0.14em; line-height: 28px;
  }
  .brand-name {
    position: absolute; left: 40px; top: 68px; width: 130px;
    display: flex; align-items: center; gap: 7px;
    font-weight: 700; font-size: 15px; line-height: 17px; color: var(--olive);
  }
  .brand-dot { width: 12px; height: 12px; border-radius: 50%; background: var(--olive); flex: none; }
  .uses {
    position: absolute; left: 197px; top: 73px; padding-left: 10px;
    border-left: 1.2px solid var(--rule);
    list-style: none; font-size: 11.5px; line-height: 14.4px;
  }

  .directions { position: absolute; left: 781px; top: 9px; width: 192px; text-align: justify; font-size: 10.8px; line-height: 12px; }
  .directions em { color: var(--olive); font-weight: 600; }
  .directions p + p { margin-top: 12px; }

  .weight { position: absolute; left: 871px; top: 118px; font-weight: 700; font-size: 10.6px; }

  .notice { position: absolute; left: 997px; top: 9px; width: 164px; font-size: 9.6px; line-height: 9.8px; text-align: justify; }
  .made-in { position: absolute; left: 997px; top: 82px; width: 164px; text-align: center; font-style: italic; font-weight: 600; color: var(--olive); font-size: 10.6px; }
  .distributor { position: absolute; left: 997px; top: 102px; width: 164px; text-align: center; font-weight: 700; font-size: 10.6px; }
  .website { position: absolute; left: 997px; top: 118px; width: 164px; text-align: center; font-size: 10.6px; }
</style>
</head>
<body>
  <section class="label">
    <div class="ingredients">
      <h3>INGREDIENT LIST:</h3>
      <h4>Wildcrafted Ingredients:</h4>
      <p>Ashwagandha Root, Peppermint Leaf, Hops Flowers, St. John’s Wort Herb, Arnica Flowers, Green Tea Leaf, Alfalfa Leaf, Dandelion Root, Burdock Root, Chickweed Herb, Chaparral Leaf, Yarrow Flowers, Boneset Herb, Moringa Leaf, Meadowsweet Herb, Nettle Leaf.</p>
      <h4>Organic Ingredients:</h4>
      <p>Olive Oil, Aloe Leaf, Sweet Birch Bark, Helichrysum Flowers, Holy Basil Leaf, Borage Herb, Ginger Root, Angelica Root, White Willow Bark, Mustard Seed, Beeswax, Vitamin E, Essential Oils.</p>
    </div>

    <div class="brand-panel">
      <h1 class="product-name">CALMWICK BALM</h1>
      <div class="brand-name"><span class="brand-dot"></span><span>Brookmere Herbal</span></div>
      <ul class="uses">
        <li>Muscle Aches</li>
        <li>Arthritis</li>
        <li>Tendonitis</li>
        <li>Headaches</li>
      </ul>
    </div>

    <div class="directions">
      <p><em>To Use:</em> For muscle aches, arthritis and tendonitis, massage into affected area. For tension headache apply to neck, temples and forehead.</p>
      <p>Store in a cool and dry place, away from direct heat and sunlight.</p>
    </div>
    <p class="weight">WEIGHT: 1.75 OZ</p>

    <p class="notice">This product is not intended to diagnose, treat, cure or prevent any disease. Not regulated by the NQB. Please consult your health care practitioner before using product. Discontinue use if any adverse reaction occurs.</p>
    <p class="made-in">- Made in the USA -</p>
    <p class="distributor">DIST. BY: BROOKMERE HERBAL</p>
    <p class="website">www.brookmereherbal.com</p>
  </section>
</body>
</html>
```